Lawnmowing and maintenance business card and letterhead design

We need a business card design and a letter head design for a new company we are starting up.

I would like to include pictures of a cartoon ride on mower with a few tools on board, a cartoon person vacuuming staircase and a cartoon person dusting.

Our business will be handling looking after unit public areas, ie garden maintenance - mowing, trimming trees, blowing leaves.
Also dusting, vacuuming, window cleaning.

Industry/Entity Type

Business

Contact Information for Business Card

Tolvane lawnmowing and property maintenance
14 Barlowe Crescent
Mount Pritchard NSW 2170
0491726048
0478301652

Requirements
Must have
• Must have the business name, business address, abn number 64 907 518 243, business phone numbers pictures as above

```html
<!DOCTYPE html>
<html lang="en">
<head>
<meta charset="UTF-8">
<title>Tolvane Lawnmowing and Property Maintenance – Business Card</title>
<link href="https://fonts.googleapis.com/css2?family=Cinzel:wght@500&family=PT+Sans:wght@400;700&display=swap" rel="stylesheet">
<style>
  :root {
    --green: #116b2e;
    --green-dark: #0c5a25;
    --card: #f3f3f1;
    --ink: #1c1c1c;
    --backdrop: #2a2a2a;
    --mower-green: #1f7a3a;
    --mower-grey: #d4d4d2;
  }
  * { margin: 0; padding: 0; box-sizing: border-box; }
  html, body {
    width: 1200px; height: 799px; overflow: hidden;
    background: var(--backdrop);
  }
  .canvas {
    position: relative; width: 1200px; height: 799px;
    display: flex; align-items: center; justify-content: center;
  }
  .business-card {
    position: relative; width: 440px; height: 720px;
    background: var(--card); overflow: hidden;
  }
  .header-band {
    position: absolute; top: 0; left: 0; width: 440px; height: 170px;
  }
  .company-name {
    position: absolute; top: 34px; left: 0; width: 100%;
    text-align: center; color: #fff;
    font-family: "Cinzel", serif; font-weight: 500;
    font-size: 19px; line-height: 1.25; letter-spacing: 1.5px;
    text-transform: uppercase;
  }
  .contact {
    position: absolute; top: 205px; left: 66px;
    font-family: "PT Sans", sans-serif; color: var(--ink);
  }
  .person-name {
    color: var(--green); font-weight: 700; font-size: 34px; line-height: 1;
  }
  .person-role { font-size: 20px; margin-top: 2px; margin-left: 24px; }
  .phones { font-size: 20px; line-height: 1.2; margin-top: 18px; margin-left: 34px; }
  .address { font-size: 21px; line-height: 1.2; margin-top: 28px; margin-left: 10px; }
  .mascot-art {
    position: absolute; left: 0; bottom: 0; width: 440px; height: 300px;
  }
</style>
</head>
<body>
<main class="canvas">
  <article class="business-card">
    <svg class="header-band" viewBox="0 0 440 170" aria-hidden="true">
      <path d="M0 0 H440 V150 Q220 95 0 128 Z" fill="var(--green)"/>
    </svg>
    <h1 class="company-name">Tolvane Lawnmowing and<br>Property Maintenance</h1>

    <section class="contact">
      <p class="person-name">Callum Hartley</p>
      <p class="person-role">Managing Director</p>
      <p class="phones">0491726048<br>0478301652</p>
      <p class="address">14 Barlowe Crescent Mount<br>Ellery, NSW 2193</p>
    </section>

    <svg class="mascot-art" viewBox="0 0 440 300" role="img"
         aria-label="Cartoon green lawnmower character holding garden tools">
      <defs>
        <linearGradient id="mascotTone" x1="0" y1="0" x2="1" y2="1">
          <stop offset="0" stop-color="var(--mower-grey)"/>
          <stop offset="0.55" stop-color="var(--mower-green)"/>
          <stop offset="1" stop-color="var(--green-dark)"/>
        </linearGradient>
      </defs>
      <rect x="0" y="40" width="440" height="260" fill="url(#mascotTone)" opacity="0.85"/>
    </svg>
  </article>
</main>
</body>
</html>
```